Flyer design for webdesign company

create a flyer that can be printed or sent as an email. The flyer needs to be professional, modern and engaging.

Reason: opportunity for all designers to get their designs in.

Target Market(s)

business owners that do not have a website

Industry/Entity Type

It Company

Font styles to use
Sans Serif

```html
<!DOCTYPE html>
<html lang="en">
<head>
<meta charset="utf-8">
<title>Novasites – Website Flyer</title>
<link rel="stylesheet" href="https://fonts.googleapis.com/css2?family=Open+Sans:wght@400;600;700&family=Roboto+Condensed:wght@400;700&display=swap">
<style>
  :root {
    --orange: #f7941d;
    --charcoal: #3a3a3c;
    --headline: #58585a;
    --body-text: #444446;
    --paper: #f3f3f3;
    --white: #ffffff;
    --rule: #c4c4c4;
  }
  * { margin: 0; padding: 0; box-sizing: border-box; }
  html, body { width: 935px; height: 1200px; overflow: hidden; background: var(--paper); }
  .flyer {
    position: relative;
    width: 935px;
    height: 1200px;
    overflow: hidden;
    background: var(--paper);
    font-family: "Open Sans", Arial, sans-serif;
  }
  .hero-photo {
    position: absolute;
    left: 0; top: 0;
    width: 935px; height: 500px;
    background: linear-gradient(100deg, #e9e6e2 0%, #f7f7f7 35%, #dcdcdc 60%, #f2f2f2 100%);
  }
  .shapes { position: absolute; left: 0; top: 0; }

  .brand {
    position: absolute;
    right: 48px; top: 58px;
    display: flex; align-items: center; gap: 10px;
    font-family: "Open Sans", Arial, sans-serif;
    font-weight: 700;
    font-size: 24px;
    color: var(--orange);
  }
  .brand-dot { width: 22px; height: 22px; border-radius: 50%; background: var(--orange); }

  .price-badge {
    position: absolute;
    left: 697px; top: 328px;
    width: 144px; height: 144px;
    border-radius: 50%;
    background: var(--orange);
    box-shadow: 0 0 0 12px #d7d7d7;
    color: var(--white);
    font-family: "Roboto Condensed", Arial, sans-serif;
    font-weight: 700;
    text-align: center;
    display: flex; flex-direction: column; justify-content: center;
  }
  .price-badge .only { font-size: 28px; line-height: 1; }
  .price-badge .only strong { font-size: 48px; }
  .price-badge .per-day { font-size: 28px; line-height: 1.2; }

  .headline {
    position: absolute;
    left: 34px; top: 546px;
    font-family: "Roboto Condensed", Arial, sans-serif;
    font-weight: 700;
    font-size: 42px;
    line-height: 54px;
    color: var(--headline);
  }

  .benefits {
    position: absolute;
    left: 37px; top: 677px;
    list-style: none;
  }
  .benefits li {
    display: flex; align-items: center;
    height: 58px;
    font-size: 16.5px;
    color: var(--body-text);
  }
  .benefits .tick { width: 34px; height: 34px; margin-right: 12px; flex: none; }

  .watermark {
    position: absolute;
    left: 345px; top: 940px;
    display: flex; flex-direction: column; align-items: center; gap: 14px;
    opacity: 0.09;
    color: var(--orange);
    font-weight: 700;
    font-size: 40px;
  }
  .watermark-dot { width: 120px; height: 120px; border-radius: 50%; background: var(--orange); }

  .offer {
    position: absolute;
    left: 617px; top: 573px;
    width: 318px;
    text-align: center;
    color: var(--white);
    font-weight: 700;
  }
  .offer .pricing-title {
    font-family: "Roboto Condensed", Arial, sans-serif;
    color: var(--orange);
    font-size: 38px;
    line-height: 48px;
  }
  .offer .pricing-detail { font-size: 19px; line-height: 29px; margin-top: 6px; }
  .offer .pitch { font-size: 19.5px; line-height: 29px; margin-top: 80px; }
  .offer .call-label {
    font-family: "Roboto Condensed", Arial, sans-serif;
    color: var(--orange);
    font-size: 22px;
    margin-top: 66px;
  }
  .offer .phone {
    display: flex; justify-content: center; align-items: center; gap: 10px;
    color: var(--orange);
    font-family: "Roboto Condensed", Arial, sans-serif;
    font-size: 30px;
    margin-top: 8px;
  }
  .offer .phone svg { width: 30px; height: 30px; }
  .offer .site { font-size: 19.5px; margin-top: 30px; }

  .footer-band {
    position: absolute;
    left: 0; bottom: 0;
    width: 935px; height: 62px;
    background: var(--orange);
    color: var(--white);
    font-weight: 700;
    font-size: 29px;
    letter-spacing: 3px;
    text-align: center;
    line-height: 62px;
  }
</style>
</head>
<body>
<main class="flyer">
  <div class="hero-photo" role="img" aria-label="Photo of a smiling businesswoman with glasses beside a desktop, laptop, tablet and phone showing a client website"></div>

  <svg class="shapes" width="935" height="1200" viewBox="0 0 935 1200" aria-hidden="true">
    <path d="M0,452 C170,500 420,515 640,470 L935,470 L935,1200 L0,1200 Z" fill="var(--paper)"/>
    <path d="M0,428 C160,475 400,494 640,452 L640,470 C420,512 170,498 0,452 Z" fill="var(--orange)"/>
    <path d="M0,418 C160,463 400,482 650,440" fill="none" stroke="var(--rule)" stroke-width="2"/>
    <path d="M617,1095 L935,1095 L935,372 C850,378 700,400 617,470 Z" fill="var(--charcoal)"/>
  </svg>

  <div class="brand"><span class="brand-dot"></span>novasites</div>

  <div class="price-badge">
    <div class="only">ONLY <strong>$3</strong></div>
    <div class="per-day">A DAY</div>
  </div>

  <h1 class="headline">ATTRACT MORE CUSTOMERS<br>MAKE MORE MONEY</h1>

  <div class="watermark" aria-hidden="true"><span class="watermark-dot"></span>novasites</div>

  <ul class="benefits">
    <li><svg class="tick" viewBox="0 0 34 34"><rect width="34" height="34" rx="4" fill="var(--orange)"/><path d="M8 17 L14 23 L27 9" fill="none" stroke="#fff" stroke-width="4"/></svg>97% of people look online for businesses. You need a website</li>
    <li><svg class="tick" viewBox="0 0 34 34"><rect width="34" height="34" rx="4" fill="var(--orange)"/><path d="M8 17 L14 23 L27 9" fill="none" stroke="#fff" stroke-width="4"/></svg>You’re losing many customers by not having a website</li>
    <li><svg class="tick" viewBox="0 0 34 34"><rect width="34" height="34" rx="4" fill="var(--orange)"/><path d="M8 17 L14 23 L27 9" fill="none" stroke="#fff" stroke-width="4"/></svg>Beat your competition with better visibility and credibility</li>
    <li><svg class="tick" viewBox="0 0 34 34"><rect width="34" height="34" rx="4" fill="var(--orange)"/><path d="M8 17 L14 23 L27 9" fill="none" stroke="#fff" stroke-width="4"/></svg>BEAUTIFUL WEBSITES AVAILABLE NOW</li>
    <li><svg class="tick" viewBox="0 0 34 34"><rect width="34" height="34" rx="4" fill="var(--orange)"/><path d="M8 17 L14 23 L27 9" fill="none" stroke="#fff" stroke-width="4"/></svg>Smart, clean website designs ($3000 Value. No extra charge)</li>
    <li><svg class="tick" viewBox="0 0 34 34"><rect width="34" height="34" rx="4" fill="var(--orange)"/><path d="M8 17 L14 23 L27 9" fill="none" stroke="#fff" stroke-width="4"/></svg>Limited to ONLY 4 WEBSITES per area. Don’t miss out!</li>
    <li><svg class="tick" viewBox="0 0 34 34"><rect width="34" height="34" rx="4" fill="var(--orange)"/><path d="M8 17 L14 23 L27 9" fill="none" stroke="#fff" stroke-width="4"/></svg>Social Media setup options (Findly &amp; Chatterbox)</li>
  </ul>

  <section class="offer">
    <h2 class="pricing-title">PRICING:</h2>
    <p class="pricing-detail">ONLY $99/MONTH<br>(THAT’S $3.30/DAY)</p>
    <p class="pitch">Stop wasting money<br>on mailers and print<br>advertising.</p>
    <p class="call-label">CALL TODAY</p>
    <p class="phone">
      <svg viewBox="0 0 30 30"><circle cx="15" cy="15" r="13" fill="none" stroke="var(--orange)" stroke-width="2.5"/><path d="M10 8 L13 8 L14 12 L12 13.5 C13 16 14 17 16.5 18 L18 16 L22 17 L22 20 C22 21 21 22 20 22 C14 21.5 8.5 16 8 10 C8 9 9 8 10 8 Z" fill="var(--orange)"/></svg>
      1-800-555-0142
    </p>
    <p class="site">www.brightpage-web.com</p>
  </section>

  <footer class="footer-band">www.brightpage-web.com</footer>
</main>
</body>
</html>
```